Menu Board and Flyer for a Poke Restaurant

We need for our new Menu board for a Poke restaurant. There will be 2 separate boards. 1 Board for Speciality items, the second for "Build your Own". The menu boards will be installed on a wall.

The first board is going to be 36 W x 48 H inches. The second board will be 72 W x 48 H inches.

I would also like to consolidate the board into a one Page menu flyer that can be printed on an 11 inches x 14 inches Page.

The goal is to have customers focus on the ease of ordering.
We have attached a sample design idea for reference and our logo options. Including the logo is optional.

I have included some sample menus by other companies as attachment and referance.

Files need to include any special fonts used in the design.

Target Market(s)

Young Professionals who love eating healthy, trendy, delicious new food options.

Industry/Entity Type

Fast Food Restaurant

Font styles to use
Serif
Sans Serif

Requirements
Must have
• Simple
• Clean design - NOT busy
• Fun
• Easy to follow
• Highlight a step by step ordering process.
• Light background color
• Files need to include any special fonts used in the design.
Should not have
• script fonts

```html
<!DOCTYPE html>
<html lang="en">
<head>
<meta charset="utf-8">
<title>Tideline Poke Menu Boards and Flyer</title>
<link href="https://fonts.googleapis.com/css2?family=Bebas+Neue&family=Open+Sans:wght@400;600&family=Pathway+Gothic+One&display=swap" rel="stylesheet">
<style>
:root{
  --backdrop:#eef2f3;
  --sea-mist:#dbe7ec;
  --panel:#f8fbfc;
  --ink:#3e4c57;
  --aqua:#6fc3df;
  --aqua-soft:#a7d6e6;
  --icon:#cdd9df;
  --rule:#e3ecef;
}
*{box-sizing:border-box;margin:0;padding:0}
html,body{width:836px;height:1200px;overflow:hidden}
body{background:var(--backdrop);position:relative;font-family:'Open Sans',sans-serif}

.board{position:absolute;left:159px;width:478px;height:357px;background:var(--sea-mist)}
.board--specialities{top:32px}
.board--build{top:420px}
.board-title{position:absolute;right:14px;top:14px;font:48px/1 'Bebas Neue',sans-serif;color:var(--ink);letter-spacing:1px}
.board--build .board-title{font-size:54px;letter-spacing:2px;top:12px}

.logo{position:absolute;left:18px;top:8px;width:64px;height:64px;border:2px solid var(--aqua);border-radius:50%;display:flex;align-items:center;justify-content:center;font:13px/1 'Pathway Gothic One',sans-serif;color:var(--aqua);letter-spacing:.5px;text-align:center}

.panel{position:absolute;left:8px;top:79px;width:461px;height:266px;background:var(--panel);box-shadow:0 1px 2px rgba(62,76,87,.12);overflow:hidden}
.panel-arrows{position:absolute;left:0;top:0;width:461px;height:266px}

.step{position:absolute;left:18px;width:60px;height:60px;border:1.5px solid var(--aqua-soft);border-radius:50%}
.step-kicker{position:absolute;left:16px;top:12px;font:600 6px/1 'Open Sans',sans-serif;color:var(--aqua-soft);text-transform:uppercase;white-space:nowrap}
.step-name{position:absolute;left:-3px;top:18px;white-space:nowrap;font:24px/1 'Bebas Neue',sans-serif;color:var(--aqua)}
.step-name b{font-weight:400;font-size:32px;margin-right:1px}
.step--compact{width:44px;height:44px}
.step--compact .step-kicker{left:10px;top:7px;font-size:5px}
.step--compact .step-name{top:11px;font-size:21px}
.step--compact .step-name b{font-size:27px}

.item{position:absolute;font:12px/1 'Pathway Gothic One',sans-serif;color:var(--ink);letter-spacing:.6px;text-transform:uppercase;white-space:nowrap}
.desc{display:block;font:6.5px/1.25 'Open Sans',sans-serif;color:var(--aqua-soft);text-transform:none;letter-spacing:0;margin-top:2px;width:72px;white-space:normal}
.rule{position:absolute;left:148px;width:240px;height:1px;background:var(--rule)}

.option-list{position:absolute;list-style:none;font:11px/13px 'Pathway Gothic One',sans-serif;color:var(--ink);letter-spacing:.6px;text-transform:uppercase;white-space:nowrap}
.num{color:var(--aqua-soft);font-size:8.5px;margin-right:5px;letter-spacing:0}
.note{font:6px 'Open Sans',sans-serif;color:var(--aqua-soft);text-transform:none;letter-spacing:0;margin-left:8px}

.icon{position:absolute;fill:var(--icon)}

.cover{position:absolute;left:102px;top:794px;width:288px;height:366px;background:var(--sea-mist)}
.cover .logo{left:90px;top:92px;width:108px;height:108px;font-size:20px;border-width:2.5px}
.cover-title{position:absolute;left:0;right:0;top:297px;text-align:center;font:24px/1 'Bebas Neue',sans-serif;color:var(--ink);letter-spacing:1.5px}
.cover-rule{position:absolute;left:54px;width:180px;height:1px;background:var(--aqua-soft);top:322px}
.cover-rule--lower{top:326px;left:74px;width:140px}

.flyer{position:absolute;left:405px;top:794px;width:287px;height:366px;background:var(--sea-mist)}
.flyer .logo{left:14px;top:5px;width:36px;height:36px;font-size:8px;border-width:1.5px}
.flyer-title{position:absolute;left:78px;font:28px/1 'Bebas Neue',sans-serif;color:var(--ink);letter-spacing:.5px}
.flyer-title--specialities{top:12px}
.flyer-title--build{top:184px}
.flyer .panel{left:18px;transform:scale(.545);transform-origin:0 0}
.flyer .panel--specialities{top:44px}
.flyer .panel--build{top:216px}
</style>
</head>
<body>

<!-- Board one: house specialities -->
<section class="board board--specialities">
  <div class="logo">TIDELINE<br>POKE</div>
  <h1 class="board-title">House Specialities</h1>
  <div class="panel panel--specialities">
    <svg class="panel-arrows" viewBox="0 0 461 266" fill="none" stroke="#a7d6e6" stroke-width="1.3">
      <path d="M78 80 C92 96 92 112 80 128"/><path d="M80 128 l1 -7 M80 128 l6 -3"/>
      <path d="M18 162 C10 176 10 188 18 200"/><path d="M18 200 l-6 -2 M18 200 l0 -6"/>
    </svg>
    <div class="step" style="top:18px"><span class="step-kicker">Choose your</span><span class="step-name"><b>1</b>SPECIALITY</span></div>
    <div class="step" style="top:118px"><span class="step-kicker">Choose your</span><span class="step-name"><b>2</b>STYLE</span></div>
    <div class="step" style="top:191px"><span class="step-kicker">Choose your</span><span class="step-name"><b>3</b>BASE</span></div>

    <div class="item" style="left:148px;top:23px">Lava Hot<span class="desc">Description of the item goes here</span></div>
    <div class="item" style="left:148px;top:55px">Classic Hawaiian<span class="desc">Description of the item goes here</span></div>
    <div class="item" style="left:148px;top:87px">Sweet &amp; Spicy<span class="desc">Description of the item goes here</span></div>
    <div class="item" style="left:244px;top:23px">Salmon<span class="desc">Description of the item goes here</span></div>
    <div class="item" style="left:244px;top:55px">Hamachi<span class="desc">Description of the item goes here</span></div>
    <div class="item" style="left:244px;top:87px">Cracy Kimchi<span class="desc">Description of the item goes here</span></div>
    <div class="item" style="left:327px;top:23px">Wasabi Lover<span class="desc">Description of the item goes here</span></div>
    <div class="item" style="left:327px;top:55px">Ginger Ginger<span class="desc">Description of the item goes here</span></div>

    <div class="rule" style="top:117px"></div>

    <div class="item" style="left:148px;top:133px">Classic Bowl<span class="desc">Regular or Large</span></div>
    <div class="item" style="left:148px;top:157px">Crunchy Bowl<span class="desc" style="width:90px">One size, Tostada Style</span></div>
    <div class="item" style="left:244px;top:133px">Surfer Style<span class="desc" style="width:90px">Poke served taco style</span></div>
    <div class="item" style="left:244px;top:157px">Just Poke<span class="desc" style="width:120px">no base - 1lb of your favorite poke</span></div>

    <div class="rule" style="top:188px"></div>

    <div class="item" style="left:148px;top:211px">White Rise</div>
    <div class="item" style="left:148px;top:225px">Brown Rice</div>
    <div class="item" style="left:244px;top:211px">Black Rice</div>
    <div class="item" style="left:327px;top:211px">Mixed Greens</div>

    <svg class="icon" style="left:420px;top:30px" width="26" height="26" viewBox="0 0 26 26"><circle cx="13" cy="13" r="11"/></svg>
    <svg class="icon" style="left:418px;top:136px" width="30" height="24" viewBox="0 0 30 24"><path d="M1 10 H29 A14 13 0 0 1 1 10 Z"/><rect x="10" y="2" width="2" height="6"/><rect x="16" y="1" width="2" height="7"/></svg>
    <svg class="icon" style="left:418px;top:201px" width="30" height="30" viewBox="0 0 30 30"><circle cx="15" cy="15" r="14"/></svg>
  </div>
</section>

<!-- Board two: build your own -->
<section class="board board--build">
  <div class="logo">TIDELINE<br>POKE</div>
  <h1 class="board-title">Build Your Own</h1>
  <div class="panel panel--build">
    <svg class="panel-arrows" viewBox="0 0 461 266" fill="none" stroke="#a7d6e6" stroke-width="1.2">
      <path d="M16 48 C10 56 10 62 18 68"/><path d="M16 98 C10 106 10 112 18 118"/>
      <path d="M16 148 C10 156 10 162 18 168"/><path d="M16 198 C10 206 10 214 18 220"/>
    </svg>
    <div class="step step--compact" style="top:10px"><span class="step-kicker">Choose your</span><span class="step-name"><b>1</b>STYLE</span></div>
    <div class="step step--compact" style="top:60px"><span class="step-kicker">Choose your</span><span class="step-name"><b>2</b>PROTEIN</span></div>
    <div class="step step--compact" style="top:110px"><span class="step-kicker">Choose your</span><span class="step-name"><b>3</b>TOPPINS</span></div>
    <div class="step step--compact" style="top:160px"><span class="step-kicker">Choose your</span><span class="step-name"><b>4</b>SAUCE</span></div>
    <div class="step step--compact" style="top:212px"><span class="step-kicker">Choose your</span><span class="step-name"><b>5</b>BASE</span></div>

    <ul class="option-list" style="left:105px;top:18px">
      <li><span class="num">1</span>Classic Bowl<span class="note">Regular or Large</span></li>
      <li><span class="num">2</span>Crunchy Bowl<span class="note">One size, Tostada Style</span></li>
    </ul>
    <ul class="option-list" style="left:284px;top:18px">
      <li><span class="num">3</span>Surfer Style<span class="note">Poke served taco style</span></li>
      <li><span class="num">4</span>Classic Bowl<span class="note">no base - 1lb of your favorite poke</span></li>
    </ul>

    <ul class="option-list" style="left:105px;top:63px"><li><span class="num">1</span>Ahi</li><li><span class="num">2</span>Tuna</li></ul>
    <ul class="option-list" style="left:200px;top:63px"><li><span class="num">3</span>Salmon</li><li><span class="num">4</span>Hamachi</li></ul>
    <ul class="option-list" style="left:284px;top:63px"><li><span class="num">4</span>Spicy Tuna</li><li><span class="num">5</span>Scallop</li></ul>
    <ul class="option-list" style="left:380px;top:63px"><li><span class="num">6</span>Shrimp</li></ul>

    <ul class="option-list" style="left:105px;top:109px"><li><span class="num">1</span>Crispy Onion</li><li><span class="num">2</span>Green Onion</li><li><span class="num">3</span>Sweet Onion</li></ul>
    <ul class="option-list" style="left:200px;top:109px"><li><span class="num">4</span>Masago</li><li><span class="num">5</span>Cilantro</li><li><span class="num">6</span>Cucumber</li></ul>
    <ul class="option-list" style="left:284px;top:109px"><li><span class="num">7</span>Corn</li><li><span class="num">8</span>Coconut Flakes</li><li><span class="num">9</span>Ogo</li></ul>
    <ul class="option-list" style="left:375px;top:109px"><li><span class="num">10</span>Furikake</li><li><span class="num">11</span>Panko</li><li><span class="num">12</span>Sesame Seed</li><li><span class="num">13</span>Avocado</li></ul>

    <ul class="option-list" style="left:105px;top:172px"><li><span class="num">1</span>Sesame Shoyu</li><li><span class="num">2</span>Sriracha Aioli</li></ul>
    <ul class="option-list" style="left:200px;top:172px"><li><span class="num">3</span>Wasabi Creme</li><li><span class="num">4</span>Sweet Shoyu</li></ul>
    <ul class="option-list" style="left:284px;top:172px"><li><span class="num">5</span>Wasabi Shoyu</li><li><span class="num">6</span>Ginger-Scallion</li></ul>
    <ul class="option-list" style="left:380px;top:172px"><li><span class="num">7</span>Chili Lime</li><li><span class="num">8</span>Ponzu</li><li><span class="num">9</span>Sweet Chili</li></ul>

    <ul class="option-list" style="left:105px;top:225px"><li><span class="num">1</span>White Rice</li><li><span class="num">2</span>Brown Rice</li></ul>
    <ul class="option-list" style="left:200px;top:225px"><li><span class="num">3</span>Black Rice</li><li><span class="num">4</span>Mixed Greens</li></ul>

    <svg class="icon" style="left:425px;top:226px" width="24" height="18" viewBox="0 0 30 24"><path d="M1 10 H29 A14 13 0 0 1 1 10 Z"/><rect x="10" y="2" width="2" height="6"/><rect x="16" y="1" width="2" height="7"/></svg>
  </div>
</section>

<!-- Menu cover -->
<section class="cover">
  <div class="logo">TIDELINE<br>POKE</div>
  <h2 class="cover-title">Pokehouse Menu</h2>
  <div class="cover-rule"></div>
  <div class="cover-rule cover-rule--lower"></div>
</section>

<!-- One page flyer -->
<section class="flyer">
  <div class="logo">TIDELINE<br>POKE</div>
  <h2 class="flyer-title flyer-title--specialities">House Specialities</h2>
  <div class="panel panel--specialities">
    <svg class="panel-arrows" viewBox="0 0 461 266" fill="none" stroke="#a7d6e6" stroke-width="1.3">
      <path d="M78 80 C92 96 92 112 80 128"/><path d="M18 162 C10 176 10 188 18 200"/>
    </svg>
    <div class="step" style="top:18px"><span class="step-kicker">Choose your</span><span class="step-name"><b>1</b>SPECIALITY</span></div>
    <div class="step" style="top:118px"><span class="step-kicker">Choose your</span><span class="step-name"><b>2</b>STYLE</span></div>
    <div class="step" style="top:191px"><span class="step-kicker">Choose your</span><span class="step-name"><b>3</b>BASE</span></div>
    <div class="item" style="left:148px;top:23px">Lava Hot<span class="desc">Description of the item goes here</span></div>
    <div class="item" style="left:148px;top:55px">Classic Hawaiian<span class="desc">Description of the item goes here</span></div>
    <div class="item" style="left:148px;top:87px">Sweet &amp; Spicy<span class="desc">Description of the item goes here</span></div>
    <div class="item" style="left:244px;top:23px">Salmon<span class="desc">Description of the item goes here</span></div>
    <div class="item" style="left:244px;top:55px">Hamachi<span class="desc">Description of the item goes here</span></div>
    <div class="item" style="left:244px;top:87px">Cracy Kimchi<span class="desc">Description of the item goes here</span></div>
    <div class="item" style="left:327px;top:23px">Wasabi Lover<span class="desc">Description of the item goes here</span></div>
    <div class="item" style="left:327px;top:55px">Ginger Ginger<span class="desc">Description of the item goes here</span></div>
    <div class="rule" style="top:117px"></div>
    <div class="item" style="left:148px;top:133px">Classic Bowl<span class="desc">Regular or Large</span></div>
    <div class="item" style="left:148px;top:157px">Crunchy Bowl<span class="desc" style="width:90px">One size, Tostada Style</span></div>
    <div class="item" style="left:244px;top:133px">Surfer Style<span class="desc" style="width:90px">Poke served taco style</span></div>
    <div class="item" style="left:244px;top:157px">Just Poke<span class="desc" style="width:120px">no base - 1lb of your favorite poke</span></div>
    <div class="rule" style="top:188px"></div>
    <div class="item" style="left:148px;top:211px">White Rise</div>
    <div class="item" style="left:148px;top:225px">Brown Rice</div>
    <div class="item" style="left:244px;top:211px">Black Rice</div>
    <div class="item" style="left:327px;top:211px">Mixed Greens</div>
    <svg class="icon" style="left:420px;top:30px" width="26" height="26" viewBox="0 0 26 26"><circle cx="13" cy="13" r="11"/></svg>
    <svg class="icon" style="left:418px;top:136px" width="30" height="24" viewBox="0 0 30 24"><path d="M1 10 H29 A14 13 0 0 1 1 10 Z"/></svg>
    <svg class="icon" style="left:418px;top:201px" width="30" height="30" viewBox="0 0 30 30"><circle cx="15" cy="15" r="14"/></svg>
  </div>

  <h2 class="flyer-title flyer-title--build">Build Your Own</h2>
  <div class="panel panel--build">
    <svg class="panel-arrows" viewBox="0 0 461 266" fill="none" stroke="#a7d6e6" stroke-width="1.2">
      <path d="M16 48 C10 56 10 62 18 68"/><path d="M16 98 C10 106 10 112 18 118"/>
      <path d="M16 148 C10 156 10 162 18 168"/><path d="M16 198 C10 206 10 214 18 220"/>
    </svg>
    <div class="step step--compact" style="top:10px"><span class="step-kicker">Choose your</span><span class="step-name"><b>1</b>STYLE</span></div>
    <div class="step step--compact" style="top:60px"><span class="step-kicker">Choose your</span><span class="step-name"><b>2</b>PROTEIN</span></div>
    <div class="step step--compact" style="top:110px"><span class="step-kicker">Choose your</span><span class="step-name"><b>3</b>TOPPINS</span></div>
    <div class="step step--compact" style="top:160px"><span class="step-kicker">Choose your</span><span class="step-name"><b>4</b>SAUCE</span></div>
    <div class="step step--compact" style="top:212px"><span class="step-kicker">Choose your</span><span class="step-name"><b>5</b>BASE</span></div>
    <ul class="option-list" style="left:105px;top:18px"><li>Classic Bowl<span class="note">Regular or Large</span></li><li>Crunchy Bowl<span class="note">One size, Tostada Style</span></li></ul>
    <ul class="option-list" style="left:284px;top:18px"><li>Surfer Style<span class="note">Poke served taco style</span></li><li>Classic Bowl<span class="note">no base - 1lb of your favorite poke</span></li></ul>
    <ul class="option-list" style="left:105px;top:63px"><li>Ahi</li><li>Tuna</li></ul>
    <ul class="option-list" style="left:200px;top:63px"><li>Salmon</li><li>Hamachi</li></ul>
    <ul class="option-list" style="left:284px;top:63px"><li>Spicy Tuna</li><li>Scallop</li></ul>
    <ul class="option-list" style="left:380px;top:63px"><li>Shrimp</li></ul>
    <ul class="option-list" style="left:105px;top:109px"><li>Crispy Onion</li><li>Green Onion</li><li>Sweet Onion</li></ul>
    <ul class="option-list" style="left:200px;top:109px"><li>Masago</li><li>Cilantro</li><li>Cucumber</li></ul>
    <ul class="option-list" style="left:284px;top:109px"><li>Corn</li><li>Coconut Flakes</li><li>Ogo</li></ul>
    <ul class="option-list" style="left:380px;top:109px"><li>Furikake</li><li>Panko</li><li>Sesame Seed</li><li>Avocado</li></ul>
    <ul class="option-list" style="left:105px;top:172px"><li>Sesame Shoyu</li><li>Sriracha Aioli</li></ul>
    <ul class="option-list" style="left:200px;top:172px"><li>Wasabi Creme</li><li>Sweet Shoyu</li></ul>
    <ul class="option-list" style="left:284px;top:172px"><li>Wasabi Shoyu</li><li>Ginger-Scallion</li></ul>
    <ul class="option-list" style="left:380px;top:172px"><li>Chili Lime</li><li>Ponzu</li><li>Sweet Chili</li></ul>
    <ul class="option-list" style="left:105px;top:225px"><li>White Rice</li><li>Brown Rice</li></ul>
    <ul class="option-list" style="left:200px;top:225px"><li>Black Rice</li><li>Mixed Greens</li></ul>
    <svg class="icon" style="left:425px;top:226px" width="24" height="18" viewBox="0 0 30 24"><path d="M1 10 H29 A14 13 0 0 1 1 10 Z"/></svg>
  </div>
</section>

</body>
</html>
```